Film Poster Design For Japanese Film Poster #2

The title of this colour film is KAZE YAMA TSUKI HOSHI春 夏 秋 冬Translated this is literallySpring Summer Fall Winter ... however the English title is FOUR SEASONSWe attached a series of screen shots from the film and also the computer generated Kanji characters. We will be updating the brief with the Japanese title characters which currently being hand painted.We require the post in two formats. One being the traditional poster format and the other being in a wide screen ration of 1000px by 465px. Same design.This is a drama, feature length film comprising of four separate stories. The is mixture of Japanese and English dialogue. We are looking at 2 possible designs. You can choose to submit either.1: A with lots of white space ... focussing on smaller images at the Japanese text. I have uploaded a sample poster as a very rough indication. "Stories nobody ever wrote down about the quiet ones" / "Odile Bettina Rue Ingrid" - Lots of white space.Ideally we would have liked to have had the image of the young girl in the kimono pulling on the bell rope clear cut and used on white as a single main image. However, we are not sure that the clarity or resolution of the original image is sufficient. 2: One with lots of images as you can see with the two "Bridge Of Dust" Sample posters.Obviously we are not looking for a copy of either poster, but these posters are a guide to the two looks we are after.Thanks. Kaede
Hello all,Apologies for the delay. We have had to work through some naming issues.The film's English title has had to be renamed to THE LANTERNS. Please do not used TEN LANTERNS in any designed moving forward.Thanks Kaede Added Sunday, May 25, 2014

```html
<!DOCTYPE html>
<html lang="en">
<head>
<meta charset="utf-8">
<title>KAZE YAMA TSUKI HOSHI — The Lanterns</title>
<link rel="stylesheet" href="https://fonts.googleapis.com/css2?family=Lato:wght@300;400&family=Noto+Sans+JP:wght@400;900&display=swap">
<style>
  :root {
    --paper: #ffffff;
    --ink: #0b0b0b;
    --taupe: #8c8074;
    --city-dark: #1c1712;
    --city-glow: #c98a45;
    --leaf-dark: #2a1a0e;
    --leaf-warm: #c0652a;
    --leaf-gold: #e0a15a;
    --kanji-light: #c9d0e4;
    --kanji-mid: #7a829a;
  }
  * { margin: 0; padding: 0; box-sizing: border-box; }
  html, body { width: 812px; height: 1200px; overflow: hidden; background: var(--paper); }
  .poster { position: relative; width: 812px; height: 1200px; background: var(--paper); overflow: hidden; }
  .scene { position: absolute; left: 0; width: 812px; }
  .scene--city { top: 0; height: 200px; }
  .scene--leaves { bottom: 0; height: 270px; }
  .hero-kanji { position: absolute; left: 0; top: 190px; width: 812px; height: 600px; }
  .hero-kanji text { font-family: "Noto Sans JP", sans-serif; font-weight: 900; }
  .title-romaji {
    position: absolute; top: 806px; width: 100%; text-align: center;
    font-family: "Lato", sans-serif; font-weight: 400; font-size: 43px;
    letter-spacing: 0.5px; color: var(--ink);
  }
  .title-kanji {
    position: absolute; top: 982px; width: 100%; text-align: center;
    font-family: "Noto Sans JP", sans-serif; font-weight: 400; font-size: 50px;
    letter-spacing: 14px; padding-left: 14px; color: var(--ink);
  }
  .title-english {
    position: absolute; top: 1044px; width: 100%; text-align: center;
    font-family: "Lato", sans-serif; font-weight: 300; font-size: 50px;
    color: var(--taupe); letter-spacing: 0;
  }
</style>
</head>
<body>
<main class="poster">
  <svg class="scene scene--city" viewBox="0 0 812 200" role="img" aria-label="City skyline at sunset with a brushed lower edge">
    <defs>
      <linearGradient id="cityTone" x1="0" y1="0" x2="1" y2="0">
        <stop offset="0" stop-color="var(--city-dark)"/>
        <stop offset="0.35" stop-color="#5a4330"/>
        <stop offset="0.55" stop-color="var(--city-glow)"/>
        <stop offset="0.68" stop-color="#3a2c20"/>
        <stop offset="1" stop-color="var(--city-dark)"/>
      </linearGradient>
    </defs>
    <path fill="url(#cityTone)" d="M0 0H812V60L790 70 770 62 745 80 720 72 690 84 660 70 630 76 600 66 570 72 540 62 505 70 470 58 430 66 390 56 350 64 310 60 270 72 235 80 200 92 170 108 140 120 110 135 80 150 55 168 30 182 0 196Z"/>
  </svg>

  <svg class="hero-kanji" viewBox="0 0 812 600" role="img" aria-label="Large kanji 風 filled with a photograph of a young woman">
    <defs>
      <linearGradient id="kanjiTone" x1="0" y1="0" x2="1" y2="1">
        <stop offset="0" stop-color="var(--kanji-light)"/>
        <stop offset="0.3" stop-color="var(--ink)"/>
        <stop offset="0.55" stop-color="var(--kanji-mid)"/>
        <stop offset="0.75" stop-color="var(--ink)"/>
        <stop offset="1" stop-color="var(--kanji-light)"/>
      </linearGradient>
    </defs>
    <text x="406" y="520" text-anchor="middle" font-size="560" fill="url(#kanjiTone)">風</text>
  </svg>

  <h1 class="title-romaji">KAZE YAMA TSUKI HOSHI</h1>
  <p class="title-kanji" lang="ja">風山月星</p>
  <p class="title-english">THE LANTERNS</p>

  <svg class="scene scene--leaves" viewBox="0 0 812 270" role="img" aria-label="Autumn maple leaves with a brushed upper edge">
    <defs>
      <linearGradient id="leafTone" x1="0" y1="0" x2="1" y2="1">
        <stop offset="0" stop-color="var(--leaf-warm)"/>
        <stop offset="0.4" stop-color="var(--leaf-gold)"/>
        <stop offset="0.7" stop-color="var(--leaf-warm)"/>
        <stop offset="1" stop-color="var(--leaf-dark)"/>
      </linearGradient>
    </defs>
    <path fill="url(#leafTone)" d="M0 0L20 18 40 30 60 50 85 70 110 92 140 112 175 130 210 150 250 170 300 185 350 190 400 194 450 196 500 192 550 186 600 178 640 168 680 150 710 130 740 108 770 95 795 80 812 70V270H0Z"/>
  </svg>
</main>
</body>
</html>
```